Website for The Pendry Parlour

I require a website for "The Pendry Parlour" which is a blog type business for 40+ year old women covering books, true crime, history, travel and food. It needs to support blog posts, links to social media including YouTube videos, Instagram, TikTok and Facebook. The background theme needs to be like that of a newspaper. Easy to navigate and to allow me to post blogs/videos.

```html
<!DOCTYPE html>
<html lang="en">
<head>
<meta charset="utf-8">
<title>The Pendry Parlour</title>
<link href="https://fonts.googleapis.com/css2?family=Archivo+Black&family=Poppins:wght@400;500;600;700&family=Playfair+Display:wght@500&display=swap" rel="stylesheet">
<style>
:root{
  --maroon:#7a3553;
  --ink:#111111;
  --paper:#ffffff;
  --sand:#ece9e1;
  --muted:#3a3a3a;
  --night:#0b0b0b;
  --star:#f5c518;
}
*{margin:0;padding:0;box-sizing:border-box}
html,body{width:1200px;height:4988px;overflow:hidden}
body{position:relative;background:var(--paper);font-family:'Poppins',sans-serif;color:var(--ink)}
.abs{position:absolute}
.photo{position:absolute}
.hero{left:0;top:0;width:1200px;height:750px;background:linear-gradient(160deg,#8a4a2e 0%,#b4693f 30%,#6f5d4c 55%,#3c3a36 100%)}
.hero-van{left:90px;top:270px;width:400px;height:360px;border-radius:30px;background:linear-gradient(180deg,#d9a230,#a5741b)}
.torn{position:absolute;left:0;width:1200px}
.hero-title{left:522px;top:320px;color:#fff;font-family:'Archivo Black',sans-serif;line-height:1}
.hero-title .small{font-size:50px;display:block}
.hero-title .big{font-size:108px;display:block;margin:2px 0 0 -4px}
.hero-title .mid{font-size:50px;display:block;margin-top:6px}
.btn{position:absolute;background:var(--maroon);color:#fff;font-size:15px;display:flex;align-items:center;justify-content:center}
.topbar{top:780px;font-size:12px;display:flex;align-items:center;gap:8px}
.brand{left:0;width:1200px;top:832px;text-align:center;font-family:'Poppins',sans-serif;font-weight:500;font-size:86px;letter-spacing:-2px;color:var(--ink)}
.nav{left:0;width:1200px;top:960px;display:flex;justify-content:center;gap:38px;font-size:15px;font-weight:500}
.nav .active{color:var(--maroon)}
.h2{left:0;width:1200px;text-align:center;font-size:42px;font-weight:500}
.copy{left:80px;width:1040px;text-align:center;font-size:17.5px;line-height:29px;color:var(--muted)}
.card-img{position:absolute;border-radius:4px}
.card-label{position:absolute;font-size:27px;font-weight:600;color:var(--maroon)}
.card-more{position:absolute;font-size:13px;font-weight:600}
.book{position:absolute;width:275px;height:393px;box-shadow:0 18px 30px rgba(0,0,0,.18)}
.band{left:0;top:3464px;width:1200px;height:484px;background:var(--sand)}
.nl-kicker{left:621px;top:3596px;font-size:18px;color:var(--muted)}
.nl-title{left:621px;top:3630px;font-size:38px;font-weight:500;line-height:39px}
.nl-title b{color:var(--maroon);font-weight:700}
.field{position:absolute;top:3762px;height:39px;background:#fff}
.quote{left:0;width:1200px;text-align:center}
.cta{left:112px;top:4449px;width:971px;height:200px;background:var(--maroon);border-radius:22px;color:#fff;text-align:center}
.footer{left:0;top:4615px;width:1200px;height:319px;background:var(--night);color:#fff}
.f-head{position:absolute;font-size:17px;color:var(--maroon);font-weight:500}
.f-list{position:absolute;list-style:none;font-size:12.5px;line-height:29px}
.f-contact{position:absolute;font-size:14px;display:flex;gap:12px;align-items:flex-start}
.bottom{left:0;top:4934px;width:1200px;height:54px;background:#f1f1f1;font-size:12px}
.social{display:inline-block;width:22px;height:22px;border-radius:50%;background:var(--ink);margin-left:4px;vertical-align:middle}
</style>
</head>
<body>

<div class="photo hero" role="img" aria-label="Yellow camper van driving on a desert road between red rock cliffs"></div>
<div class="photo hero-van" role="img" aria-label="Vintage yellow camper van seen from behind"></div>
<svg class="torn" style="top:720px" height="60" viewBox="0 0 1200 60" preserveAspectRatio="none"><path d="M0 22 L40 18 L80 26 L120 16 L170 24 L220 14 L260 22 L310 12 L360 24 L400 16 L450 26 L500 14 L560 22 L610 12 L660 24 L710 16 L760 26 L820 14 L870 22 L920 12 L970 24 L1020 16 L1080 26 L1130 14 L1200 22 L1200 60 L0 60 Z" fill="#fff"/></svg>

<div class="abs hero-title"><span class="small">WHERE EVERY</span><span class="big">STORY</span><span class="mid">IS WORTH READING.</span></div>
<div class="btn" style="left:519px;top:542px;width:172px;height:36px">Read More</div>

<div class="abs topbar" style="left:108px">
  <svg width="18" height="18" viewBox="0 0 24 24" fill="none" stroke="#111" stroke-width="1.6"><path d="M5 3h4l2 5-2.5 1.5a11 11 0 0 0 6 6L16 13l5 2v4a2 2 0 0 1-2 2A17 17 0 0 1 3 5a2 2 0 0 1 2-2z"/></svg>
  <span>+44 20 7946 0182</span>
  <svg style="margin-left:20px" width="18" height="14" viewBox="0 0 24 18" fill="none" stroke="#111" stroke-width="1.6"><rect x="1" y="1" width="22" height="16"/><path d="M1 1l11 9 11-9"/></svg>
  <span>info@thependryparlour.com</span>
</div>
<div class="abs topbar" style="left:1038px">
  <svg width="14" height="14" viewBox="0 0 24 24" fill="none" stroke="#111" stroke-width="2"><path d="M4 8h16l-1 13H5z"/><path d="M8 8a4 4 0 0 1 8 0"/></svg>
  <span style="display:inline-block;width:14px;height:14px;border-radius:50%;background:#111;color:#fff;font-size:9px;text-align:center;line-height:14px;margin-left:-6px">0</span>
  <svg style="margin-left:10px" width="13" height="13" viewBox="0 0 24 24" fill="none" stroke="#111" stroke-width="2.4"><circle cx="10" cy="10" r="7"/><path d="M15 15l7 7"/></svg>
</div>

<div class="abs brand">The Pendry Parlour</div>
<nav class="abs nav"><span>Home</span><span>Our Story</span><span>Categories</span><span>The Team</span><span class="active">Blog</span><span>Contact Us</span></nav>

<h2 class="abs h2" style="top:1045px">WHO WE ARE</h2>
<p class="abs copy" style="top:1117px">Lorem Ipsum is simply dummy text of the printing and typesetting industry. Lorem Ipsum has been the industry's standard dummy text ever since the 1500s, when an unknown printer took a galley of type and scrambled it to make a type specimen book. It has survived not only five centuries,<br>but also the leap into electronic typesetting, remaining essentially unchanged.</p>
<p class="abs copy" style="top:1262px">It was popularised in the 1960s with the release of Lettersheet sheets containing Lorem Ipsum passages, and more recently with desktop publishing software like Folio Layout including versions of Lorem Ipsum.</p>

<div class="photo" style="left:168px;top:1360px;width:879px;height:408px;border-radius:14px;background:linear-gradient(180deg,#c9b48a 0%,#e8c36a 45%,#3a3320 70%,#1d1a10 100%)" role="img" aria-label="Sunset over a pine forest with a dandelion seed head in the foreground"></div>

<h2 class="abs h2" style="top:1815px">30% OFF ON ONLINE ORDERS</h2>
<p class="abs copy" style="top:1883px;left:120px;width:960px">Lorem Ipsum is simply dummy text of the printing and typesetting industry. Lorem Ipsum has been the industry's standard dummy text ever since the 1500s, when an unknown printer took a galley of type and scrambled it to make a type specimen book. It has survived not only five centuries,<br>but also the leap into electronic typesetting, remaining essentially unchanged.</p>
<div class="btn" style="left:519px;top:2028px;width:172px;height:42px">Read More</div>

<div class="card-img" style="left:99px;top:2138px;width:491px;height:322px;background:linear-gradient(180deg,#5a5f66,#2a2c30)" role="img" aria-label="True crime show promo with three investigators"></div>
<div class="card-img" style="left:610px;top:2138px;width:489px;height:322px;background:linear-gradient(180deg,#3f7fc4 0%,#8fb8e0 45%,#c69a55 60%,#d9b070 100%)" role="img" aria-label="Pyramids in the desert with a camel caravan"></div>
<div class="card-label" style="left:108px;top:2468px">True Crime</div><div class="card-more" style="left:505px;top:2480px">Read More</div>
<div class="card-label" style="left:619px;top:2468px">History</div><div class="card-more" style="left:1014px;top:2480px">Read More</div>

<div class="card-img" style="left:99px;top:2527px;width:491px;height:323px;background:linear-gradient(180deg,#9cc3e2 0%,#5f7c6a 45%,#4a6a8a 70%,#7a8f4a 100%)" role="img" aria-label="Traveller with backpack overlooking a mountain lake"></div>
<div class="card-img" style="left:610px;top:2527px;width:489px;height:323px;background:linear-gradient(180deg,#8f8f86,#c23a2a 60%,#6b6b6b)" role="img" aria-label="Street food cart on a busy city street"></div>
<div class="card-label" style="left:108px;top:2857px">Travel</div><div class="card-more" style="left:505px;top:2869px">Read More</div>
<div class="card-label" style="left:619px;top:2857px">Food</div><div class="card-more" style="left:1014px;top:2869px">Read More</div>

<div class="book" style="left:120px;top:2961px;background:linear-gradient(180deg,#e9e2d4 0%,#c79a78 60%,#9b5b3f 100%)" role="img" aria-label="Book cover with a church spire over old town rooftops"></div>
<div class="book" style="left:464px;top:2961px;background:linear-gradient(180deg,#111 0%,#1c1c1c 60%,#d9d9d9 100%)" role="img" aria-label="Black book cover with a milk bottle"></div>
<div class="book" style="left:813px;top:2961px;background:linear-gradient(180deg,#123a52,#0b2434)" role="img" aria-label="Dark blue book cover with a figure reading a burning newspaper"></div>

<div class="abs band"></div>
<svg class="torn" style="top:3440px" height="30" viewBox="0 0 1200 30" preserveAspectRatio="none"><path d="M0 24 L50 18 L100 26 L160 16 L220 24 L290 14 L350 22 L420 16 L480 26 L550 15 L620 23 L690 14 L760 25 L830 16 L900 24 L970 14 L1040 23 L1110 16 L1200 24 L1200 30 L0 30 Z" fill="#ece9e1"/></svg>
<svg class="torn" style="top:3940px" height="30" viewBox="0 0 1200 30" preserveAspectRatio="none"><path d="M0 0 L1200 0 L1200 10 L1130 16 L1060 8 L990 18 L920 9 L850 17 L780 8 L710 18 L640 9 L570 16 L500 8 L430 18 L360 10 L290 17 L220 8 L150 16 L80 9 L0 15 Z" fill="#ece9e1"/></svg>

<div class="photo" style="left:87px;top:3541px;width:220px;height:358px;background:linear-gradient(180deg,#cfd9de,#6e7d82 55%,#3e4346);border:8px solid #fff;box-shadow:0 6px 16px rgba(0,0,0,.2)" role="img" aria-label="Poster of a mountain road"></div>
<div class="photo" style="left:270px;top:3580px;width:330px;height:300px;background:linear-gradient(135deg,#f4f1ea 0%,#e6ddd0 45%,#a0603c 60%,#6b3c24 100%);transform:rotate(-18deg);box-shadow:0 10px 20px rgba(0,0,0,.2)" role="img" aria-label="Open book mockup with a desert arch photograph"></div>

<div class="abs nl-kicker">Lorem ipsum dolor</div>
<div class="abs nl-title">FINDING THE PERFECT<br>TRAILS TO HIKE IS EASY<br>WITH <b>NEWSLETTER</b></div>
<div class="field" style="left:623px;width:141px"></div>
<div class="field" style="left:774px;width:139px"></div>
<div class="field" style="left:921px;width:137px;background:var(--maroon)"></div>

<div class="photo" style="left:554px;top:4054px;width:84px;height:84px;border-radius:50%;background:linear-gradient(180deg,#e8d2b0,#c98f6a);border:3px solid #fff;box-shadow:0 2px 8px rgba(0,0,0,.2)" role="img" aria-label="Reviewer portrait"></div>
<div class="abs quote" style="top:4148px;font-size:23px">What others said</div>
<div class="abs quote" style="top:4184px;font-size:20px;color:var(--star);letter-spacing:2px">★★★★★</div>
<p class="abs quote" style="top:4218px;left:200px;width:800px;font-size:14.5px;line-height:22px;color:var(--muted)">Lorem ipsum dolor sit amet, consectetur adipiscing elit, sed do eiusmod tempor incididunt ut labore et dolore magna aliqua. Lorem ipsum dolor sit amet, consectetur adipiscing elit, sed do eiusmod tempor incididunt ut labore et dolore magna aliqua.</p>
<div class="abs quote" style="top:4290px;font-size:16px;font-weight:500;letter-spacing:1px">CLARA WELLS</div>
<svg class="abs" style="left:563px;top:4328px" width="74" height="12"><circle cx="6" cy="6" r="5.5" fill="#bbb"/><circle cx="26" cy="6" r="5.5" fill="#bbb"/><circle cx="46" cy="6" r="5.5" fill="#bbb"/><circle cx="66" cy="6" r="5.5" fill="#1a3a9a"/></svg>

<div class="abs cta">
  <div style="font-size:52px;font-weight:500;margin-top:44px;line-height:60px">+1 555 240 8817</div>
  <div style="font-size:17px;line-height:24px;margin-top:6px">Ready to schedule your cleanup or have questions?<br>We'd love to hear from you.</div>
</div>

<div class="abs footer">
  <div class="f-head" style="left:99px;top:40px">Information</div>
  <ul class="f-list" style="left:99px;top:86px"><li>- Home</li><li>- Our Story</li><li>- Our Stays</li><li>- Activities</li></ul>
  <div class="f-head" style="left:304px;top:40px">About</div>
  <ul class="f-list" style="left:304px;top:86px"><li>- Agenda</li><li>- Our Charter</li><li>- The Team</li><li>- Contact</li><li>- Blog</li></ul>
  <div class="f-head" style="left:482px;top:40px">Contact us</div>
  <div class="f-contact" style="left:482px;top:101px;font-size:16px">
    <svg width="20" height="20" viewBox="0 0 24 24" fill="none" stroke="#fff" stroke-width="1.6"><path d="M5 3h4l2 5-2.5 1.5a11 11 0 0 0 6 6L16 13l5 2v4a2 2 0 0 1-2 2A17 17 0 0 1 3 5a2 2 0 0 1 2-2z"/></svg><span>+1 555 240 8817</span></div>
  <div class="f-contact" style="left:482px;top:138px">
    <svg width="20" height="15" viewBox="0 0 24 18" fill="none" stroke="#fff" stroke-width="1.6"><rect x="1" y="1" width="22" height="16"/><path d="M1 1l11 9 11-9"/></svg><span>info@thependryparlour.com</span></div>
  <div class="f-contact" style="left:482px;top:172px;font-size:13px;line-height:18px">
    <svg width="20" height="22" viewBox="0 0 24 26" fill="none" stroke="#fff" stroke-width="1.6"><path d="M12 25s8-8 8-14a8 8 0 0 0-16 0c0 6 8 14 8 14z"/><circle cx="12" cy="11" r="3"/></svg><span>Orchard Lane 14, Suite B2<br>Riverside Court<br>Millbrook 4410</span></div>
  <div class="abs" style="left:757px;top:48px;font-size:36px;font-weight:500;letter-spacing:-1px">The Pendry Parlour</div>
  <div class="abs" style="left:759px;top:102px;font-size:17px;color:var(--maroon)">Subscribe to our newsletter</div>
  <div class="abs" style="left:759px;top:142px;width:296px;height:33px;background:#fff;border:1px solid #fff">
    <div style="position:absolute;left:198px;top:0;width:98px;height:31px;border-left:1px solid #111;color:#111;font-size:11px;text-align:center;line-height:31px">Email</div>
    <div style="position:absolute;left:0;top:0;width:198px;height:31px;background:var(--night)"></div>
  </div>
  <div class="abs" style="left:761px;top:198px;width:300px;font-size:10px;font-weight:600;line-height:15px">Subscribe today and get exciting gifts and 10% off on your first order.</div>
</div>
<svg class="torn" style="top:4595px" height="30" viewBox="0 0 1200 30" preserveAspectRatio="none"><path d="M0 22 L60 14 L120 24 L190 12 L260 22 L330 15 L400 25 L470 13 L540 22 L610 14 L680 24 L750 12 L820 22 L890 15 L960 25 L1030 13 L1100 22 L1200 14 L1200 30 L0 30 Z" fill="#0b0b0b"/></svg>

<div class="abs" style="left:108px;top:4890px;width:165px;height:44px;background:#fff;color:var(--maroon);font-size:19px;font-weight:500;text-align:center;line-height:44px">CLICK HERE</div>

<div class="abs bottom">
  <span class="abs" style="left:84px;top:20px">© 2025 The Pendry Parlour</span>
  <span class="abs" style="left:930px;top:15px">Follow me: <i class="social"></i><i class="social"></i><i class="social"></i><i class="social"></i></span>
</div>

</body>
</html>
```